Everything fresh, everything new

When I take over the practice, I would like to breathe new life into the practice. I want a business card design that catches the eye and brings a breath of fresh air

```html
<!DOCTYPE html>
<html lang="de">
<head>
<meta charset="utf-8">
<title>Praxis Neuwind – Visitenkarte</title>
<link rel="stylesheet" href="https://fonts.googleapis.com/css2?family=Montserrat:wght@300;400;500;700;800&display=swap">
<style>
  :root {
    --stage: #c9c9c9;
    --stage-deep: #b3b3b3;
    --card-dark: #4a4a4c;
    --card-light: #ffffff;
    --accent: #8cc63f;
    --text-light: #ffffff;
    --text-dark: #3d3d3f;
    --radius: 22px;
  }
  * { box-sizing: border-box; margin: 0; padding: 0; }
  html, body { width: 1200px; height: 815px; overflow: hidden; }
  body {
    background: linear-gradient(160deg, var(--stage) 0%, var(--stage-deep) 100%);
    font-family: "Montserrat", sans-serif;
    position: relative;
  }
  .card {
    position: absolute;
    top: 253px;
    width: 540px;
    height: 309px;
    border-radius: var(--radius);
    overflow: hidden;
    box-shadow: 0 12px 28px rgba(0,0,0,.28);
  }
  .card--front { left: 40px; background: var(--card-light); }
  .card--back  { left: 620px; background: var(--card-dark); }

  .front-wave { position: absolute; inset: 0; width: 100%; height: 100%; }

  .brand {
    position: absolute;
    display: flex;
    align-items: center;
    gap: 10px;
    font-weight: 500;
    letter-spacing: -0.5px;
    white-space: nowrap;
  }
  .brand__dot { border-radius: 50%; background: var(--accent); flex: none; }
  .card--front .brand {
    top: 26px; left: 170px;
    font-size: 24px;
    color: var(--text-dark);
  }
  .card--front .brand__dot { width: 14px; height: 14px; }

  .card--back .brand {
    top: 50%; left: 50%;
    transform: translate(-50%, -50%);
    font-size: 44px;
    color: var(--text-light);
    gap: 14px;
  }
  .card--back .brand__dot { width: 24px; height: 24px; }

  .address {
    position: absolute;
    right: 26px; top: 150px;
    text-align: right;
    color: var(--text-light);
    font-size: 12.5px;
    line-height: 1.45;
    letter-spacing: .3px;
  }

  .person {
    position: absolute;
    left: 28px; bottom: 22px;
    color: var(--text-light);
  }
  .person__name {
    color: var(--accent);
    font-weight: 800;
    font-size: 24px;
    letter-spacing: 1px;
    line-height: 1.1;
  }
  .person__role {
    font-weight: 400;
    font-size: 12.5px;
    letter-spacing: 1px;
    margin-bottom: 12px;
  }
  .contact { list-style: none; font-size: 12.5px; line-height: 1.7; letter-spacing: .3px; }
  .contact li { display: flex; align-items: center; gap: 8px; }
  .contact svg { width: 11px; height: 11px; flex: none; }
  .icon--fill { fill: var(--accent); }
  .icon--line { fill: none; stroke: var(--accent); stroke-width: 2.4; }
</style>
</head>
<body>

  <section class="card card--front" aria-label="Visitenkarte Vorderseite">
    <svg class="front-wave" viewBox="0 0 540 309" preserveAspectRatio="none" aria-hidden="true">
      <path d="M0,140 C22,108 62,100 140,92 C260,80 372,64 420,36 C446,20 455,8 456,0 L540,0 L540,309 L0,309 Z" fill="var(--accent)"/>
      <path d="M0,152 C22,116 64,108 140,100 C262,88 380,74 428,44 C454,26 464,10 466,0 L540,0 L540,309 L0,309 Z" fill="var(--card-light)"/>
      <path d="M0,160 C22,122 66,114 142,106 C264,94 386,80 434,50 C460,32 472,12 474,0 L540,0 L540,309 L0,309 Z" fill="var(--card-dark)"/>
    </svg>

    <div class="brand">
      <span class="brand__dot"></span>
      <span class="brand__name">Praxis Neuwind</span>
    </div>

    <p class="address">Birkenweg 18<br>79098 Freiburg</p>

    <div class="person">
      <p class="person__name">LENA HARTWIG</p>
      <p class="person__role">MANAGER</p>
      <ul class="contact">
        <li>
          <svg class="icon--fill" viewBox="0 0 24 24"><path d="M6.6 10.8a15.1 15.1 0 0 0 6.6 6.6l2.2-2.2c.3-.3.7-.4 1-.2 1.1.4 2.3.6 3.6.6.6 0 1 .4 1 1V20c0 .6-.4 1-1 1A17 17 0 0 1 3 4c0-.6.4-1 1-1h3.5c.6 0 1 .4 1 1 0 1.3.2 2.5.6 3.6.1.3 0 .7-.2 1z"/></svg>
          (555) 010-2741
        </li>
        <li>
          <svg class="icon--line" viewBox="0 0 24 24"><path d="M3 5h18v14H3z M3 6l9 7 9-7"/></svg>
          hallo@neuwind-praxis.de
        </li>
        <li>
          <svg class="icon--line" viewBox="0 0 24 24"><circle cx="12" cy="12" r="9"/><path d="M3 12h18 M12 3c3 3 3 15 0 18 M12 3c-3 3-3 15 0 18"/></svg>
          www.neuwind-praxis.de
        </li>
      </ul>
    </div>
  </section>

  <section class="card card--back" aria-label="Visitenkarte Rückseite">
    <div class="brand">
      <span class="brand__dot"></span>
      <span class="brand__name">Praxis Neuwind</span>
    </div>
  </section>

</body>
</html>
```